Marlow Fields Thank-You Tag

Looking for a file that incorporates current branding/colors and says:

"Thanks for Swimming with Us!"
Marlow Fields Otters

Samples of other pieces we've done recently are attached.

Will be printed on cardstock that is
Width: 3.5 inches
Height: 2.5 inches

```html
<!DOCTYPE html>
<html lang="en">
<head>
<meta charset="utf-8">
<title>Marlow Fields Otters – Thank-You Tag</title>
<link href="https://fonts.googleapis.com/css2?family=Passion+One:wght@400;700&family=Nunito+Sans:wght@900&display=swap" rel="stylesheet">
<style>
  :root {
    --backdrop: #8a8a8a;
    --pool-blue: #2b52a3;
    --splash-pink: #e5609e;
    --foam-white: #ffffff;
    --fin-silver: #c4c4c8;
  }
  html, body {
    margin: 0;
    width: 1200px;
    height: 901px;
    overflow: hidden;
    background: var(--backdrop);
  }
  .tag {
    position: absolute;
    left: 100px;
    top: 93px;
    width: 1001px;
    height: 714px;
    background: var(--pool-blue);
    overflow: hidden;
  }
  .headline {
    position: absolute;
    margin: 0;
    text-align: center;
    font-family: "Passion One", "Arial Black", sans-serif;
    font-weight: 700;
    text-transform: uppercase;
    line-height: 1;
    white-space: nowrap;
    transform-origin: center center;
  }
  .headline-thanks {
    left: 178px;
    top: 62px;
    width: 600px;
    font-size: 165px;
    color: var(--foam-white);
    transform: rotate(-3deg) scaleX(0.94);
  }
  .banner {
    position: absolute;
    left: 323px;
    top: 216px;
    width: 378px;
    height: 105px;
  }
  .banner svg { position: absolute; inset: 0; }
  .headline-for {
    left: 0;
    top: 14px;
    width: 378px;
    font-size: 86px;
    color: var(--foam-white);
  }
  .headline-swimming {
    left: 212px;
    top: 326px;
    width: 600px;
    font-size: 110px;
    color: var(--foam-white);
    transform: rotate(-2deg) scaleX(0.88);
  }
  .headline-with-us {
    left: 208px;
    top: 432px;
    width: 600px;
    font-size: 118px;
    color: var(--splash-pink);
    transform: rotate(-3deg) scaleX(0.88);
  }
  .mascot-art {
    position: absolute;
    left: 110px;
    top: 240px;
    width: 155px;
    height: 317px;
    border-radius: 40% 40% 30% 30%;
    background: linear-gradient(160deg, var(--fin-silver) 0%, #9fa7c4 60%, var(--splash-pink) 100%);
    opacity: 0.85;
  }
  .club-seal {
    position: absolute;
    left: 757px;
    top: 336px;
    width: 204px;
    height: 204px;
    box-sizing: border-box;
    border: 12px solid var(--foam-white);
    border-radius: 50%;
    display: flex;
    align-items: center;
    justify-content: center;
    text-align: center;
  }
  .club-seal-name {
    font-family: "Nunito Sans", "Arial", sans-serif;
    font-weight: 900;
    font-size: 24px;
    line-height: 1.15;
    letter-spacing: 1px;
    text-transform: uppercase;
    color: var(--foam-white);
  }
  .wave-line {
    position: absolute;
    left: 74px;
    top: 580px;
    width: 849px;
    height: 16px;
  }
  .team-name {
    position: absolute;
    left: 0;
    top: 614px;
    width: 1001px;
    margin: 0;
    text-align: center;
    font-family: "Nunito Sans", "Arial", sans-serif;
    font-weight: 900;
    font-size: 34px;
    letter-spacing: 2px;
    text-transform: uppercase;
    color: var(--foam-white);
  }
  .team-name-mascot { color: var(--splash-pink); }
</style>
</head>
<body>
  <main class="tag">
    <div class="mascot-art" role="img" aria-label="Illustration of a leaping team mascot above a pink water splash"></div>

    <h1 class="headline headline-thanks">Thanks</h1>

    <div class="banner">
      <svg viewBox="0 0 378 105" width="378" height="105" aria-hidden="true">
        <polygon points="0,14 378,14 364,52 370,98 8,105 14,56" fill="var(--splash-pink)"/>
      </svg>
      <p class="headline headline-for">For</p>
    </div>

    <p class="headline headline-swimming">Swimming</p>
    <p class="headline headline-with-us">With Us!</p>

    <div class="club-seal">
      <span class="club-seal-name">Marlow<br>Fields</span>
    </div>

    <svg class="wave-line" viewBox="0 0 849 16" aria-hidden="true" fill="none" stroke="var(--fin-silver)" stroke-width="3" stroke-linecap="round">
      <path d="M2 9 q10.4 -7 20.8 0 t20.8 0 t20.8 0 t20.8 0 t20.8 0 t20.8 0"/>
      <path d="M147 9 q10.4 -7 20.8 0 t20.8 0 t20.8 0 t20.8 0 t20.8 0 t20.8 0"/>
      <path d="M292 9 q10.4 -7 20.8 0 t20.8 0 t20.8 0 t20.8 0 t20.8 0 t20.8 0"/>
      <path d="M437 9 q10.4 -7 20.8 0 t20.8 0 t20.8 0 t20.8 0 t20.8 0 t20.8 0"/>
      <path d="M582 9 q10.4 -7 20.8 0 t20.8 0 t20.8 0 t20.8 0 t20.8 0 t20.8 0"/>
      <path d="M722 9 q10.4 -7 20.8 0 t20.8 0 t20.8 0 t20.8 0 t20.8 0 t20.8 0"/>
    </svg>

    <p class="team-name">Marlow Fields <span class="team-name-mascot">Otters</span></p>
  </main>
</body>
</html>
```